BQN Project Signage

Need a sign to be displayed in the front of properties currently under Construction or Renovation to advertise our company information. Need it to be Professional and Contemporary. We are a Design/Build Construction Company. Information should include Company Name, email, website, phone number. Attached: Logo and company brochure, also included and inspiration images

```html
<!DOCTYPE html>
<html lang="en">
<head>
<meta charset="utf-8">
<title>BQN Construction – Project Sign</title>
<link rel="stylesheet" href="https://fonts.googleapis.com/css2?family=Montserrat:wght@500;600;700;800&display=swap">
<style>
  :root {
    --backdrop: #333333;
    --slate: #6b6b6b;
    --signal-yellow: #f2ea48;
    --ink: #0d0d0d;
    --paper: #ffffff;
  }
  * { box-sizing: border-box; margin: 0; padding: 0; }
  html, body {
    width: 1200px; height: 1200px; overflow: hidden;
    background: var(--backdrop);
    font-family: "Montserrat", sans-serif;
    color: var(--ink);
  }
  .sign {
    position: absolute; left: 247px; top: 70px;
    width: 706px; height: 1060px;
    display: flex; flex-direction: column;
  }
  .brand-panel {
    height: 514px; background: var(--slate);
    display: flex; flex-direction: column; align-items: center; justify-content: center;
    gap: 18px;
  }
  .brand-name {
    font-weight: 600; font-size: 50px; letter-spacing: 3px; color: var(--ink);
  }
  .brand-tagline {
    font-weight: 600; font-size: 24px; letter-spacing: 4px; color: var(--ink);
  }
  .divider { height: 6px; background: var(--paper); }
  .contact-panel {
    flex: 1; background: var(--signal-yellow);
    display: flex; flex-direction: column; align-items: center;
    padding-top: 16px;
  }
  .address {
    display: flex; align-items: flex-start; gap: 8px;
    font-weight: 600; font-size: 37px; line-height: 44px; text-align: center;
  }
  .icon { width: 42px; height: 42px; flex: none; margin-top: 0; }
  .address-lines span { display: block; }
  .phone-label {
    margin-top: 22px;
    background: var(--ink); color: var(--signal-yellow);
    font-weight: 700; font-size: 34px; letter-spacing: -1px; line-height: 44px;
    padding: 2px 12px; border-radius: 6px;
  }
  .phone-number {
    font-weight: 800; font-size: 80px; line-height: 86px; letter-spacing: -1px;
  }
  .web-line {
    display: flex; align-items: center; gap: 10px;
    font-weight: 500; font-size: 40px; line-height: 50px; letter-spacing: -0.5px;
  }
  .web-line.email { margin-top: 24px; }
  .web-line.site { margin-top: 8px; font-weight: 600; }
</style>
</head>
<body>
<main class="sign">
  <section class="brand-panel">
    <h1 class="brand-name">BQN CONSTRUCTION</h1>
    <p class="brand-tagline">LUXURY RENOVATIONS</p>
  </section>
  <div class="divider"></div>
  <section class="contact-panel">
    <div class="address">
      <svg class="icon" viewBox="0 0 42 42" aria-hidden="true">
        <circle cx="21" cy="21" r="21" fill="#0d0d0d"/>
        <path d="M21 8a8 8 0 0 0-8 8c0 6 8 14 8 14s8-8 8-14a8 8 0 0 0-8-8z" fill="#f2ea48"/>
        <circle cx="21" cy="16" r="3" fill="#0d0d0d"/>
        <ellipse cx="21" cy="32" rx="9" ry="2.5" fill="none" stroke="#f2ea48" stroke-width="2"/>
      </svg>
      <div class="address-lines">
        <span>4150 NE 7TH ST., STE. 310</span>
        <span>CORAL GLADES, FL 33400</span>
      </div>
    </div>
    <div class="phone-label">DIRECT</div>
    <div class="phone-number">555.201.4870</div>
    <div class="phone-label">OFFICE</div>
    <div class="phone-number">555.308.2264</div>
    <div class="web-line email">
      <svg class="icon" viewBox="0 0 42 42" aria-hidden="true">
        <circle cx="21" cy="21" r="21" fill="#0d0d0d"/>
        <rect x="10" y="15" width="22" height="15" fill="none" stroke="#f2ea48" stroke-width="2"/>
        <path d="M10 15l11 9 11-9" fill="none" stroke="#f2ea48" stroke-width="2"/>
      </svg>
      <span>elias@bqnconstruction.com</span>
    </div>
    <div class="web-line site">
      <svg class="icon" viewBox="0 0 42 42" aria-hidden="true">
        <circle cx="21" cy="21" r="21" fill="#0d0d0d"/>
        <circle cx="21" cy="21" r="11" fill="none" stroke="#f2ea48" stroke-width="2"/>
        <ellipse cx="21" cy="21" rx="5" ry="11" fill="none" stroke="#f2ea48" stroke-width="2"/>
        <path d="M10 21h22M12 15h18M12 27h18" stroke="#f2ea48" stroke-width="2"/>
      </svg>
      <span>www.bqnconstruction.com</span>
    </div>
  </section>
</main>
</body>
</html>
```